May/June Newsletter

We require a newsletter with as much infographic as possible

Attached is our previous newsletter as an example.

ONLY USE THE DATA IN EPC CHALLENGES

Target Market(s)

property market

Requirements
Must have
• Company colours and logo from
www.verdanthaus.co.uk

be similar to our previous newsletter. copy attached.

must have a screenshot of VHConnect attached

```html
<!DOCTYPE html>
<html lang="en">
<head>
<meta charset="utf-8">
<title>May/June Newsletter – Verdant Haus</title>
<link href="https://fonts.googleapis.com/css2?family=Montserrat:wght@400;500;600;700;800&family=Open+Sans:wght@400;600&display=swap" rel="stylesheet">
<style>
:root{
  --page:#2b2b2b;
  --paper:#ffffff;
  --green:#3cb54a;
  --green-dark:#2e9a3b;
  --ink:#333333;
  --muted:#8a8a8a;
  --heading-grey:#c9c9c9;
  --band:#4a4a4a;
  --panel:#ececec;
  --footer:#3a3a3a;
  --navy:#0a1a6b;
}
*{box-sizing:border-box;margin:0;padding:0}
html,body{width:1200px;height:2962px;overflow:hidden;background:var(--page);font-family:"Open Sans",Arial,sans-serif;color:var(--ink)}
.issue-title{position:absolute;top:52px;left:0;width:1200px;text-align:center;color:#fff;font-family:"Montserrat",sans-serif;font-weight:400;font-size:30px;letter-spacing:7px}
.sheet{position:absolute;top:133px;left:270px;width:661px;height:2749px;background:var(--paper);overflow:hidden}
.masthead{position:absolute;top:0;left:0;width:661px;height:106px;background:#fff}
.brand{position:absolute;left:33px;top:22px}
.brand-name{font-family:"Montserrat",sans-serif;font-weight:800;font-size:40px;color:#555;letter-spacing:-1px;line-height:1;display:flex;align-items:center;gap:8px}
.brand-dot{width:16px;height:16px;border-radius:50%;background:var(--green);display:inline-block}
.brand-tag{font-family:"Montserrat",sans-serif;font-size:11.5px;letter-spacing:3.3px;color:#999;margin-top:6px}
.contact{position:absolute;right:34px;top:33px;font-family:"Montserrat",sans-serif;font-size:12.5px;color:#777;line-height:24px}
.contact div{display:flex;align-items:center;gap:10px}
.hero{position:absolute;top:106px;left:0;width:661px;height:228px;background:linear-gradient(180deg,#0d1e8a 0%,#1c3bc4 45%,#0a1450 80%,#050a2a 100%)}
.hero-title{position:absolute;left:0;right:0;top:176px;text-align:center;color:#fff;font-family:"Montserrat",sans-serif;font-weight:500;font-size:19px;letter-spacing:.4px}
.hero-sub{position:absolute;left:0;right:0;top:201px;text-align:center;color:var(--green);font-family:"Montserrat",sans-serif;font-size:13px;letter-spacing:.3px}
.section-title{position:absolute;top:349px;left:0;width:661px;text-align:center;font-family:"Montserrat",sans-serif;font-weight:800;font-size:56px;color:var(--heading-grey);letter-spacing:1px}
.april{position:absolute;top:442px;left:32px;width:596px;height:163px;border:2px solid var(--green);border-radius:8px}
.april-tab{position:absolute;top:-2px;left:172px;width:254px;height:32px;background:var(--green);clip-path:polygon(0 0,100% 0,94% 100%,6% 100%);color:#fff;font-family:"Montserrat",sans-serif;font-weight:700;font-size:25px;display:flex;align-items:center;justify-content:center;gap:10px}
.april-col{position:absolute;top:56px;font-size:11.3px;line-height:13.5px;color:#333}
.april-col.left{left:90px;width:175px}
.april-col.right{left:376px;width:196px}
.april-icon{position:absolute;top:56px}
.april-divider{position:absolute;left:290px;top:48px;width:1px;height:98px;background:#bbb}
.band-grey{position:absolute;top:637px;left:0;width:661px;height:47px;background:var(--band);color:#fff;font-family:"Montserrat",sans-serif;font-weight:700;font-size:24px;display:flex;align-items:center;justify-content:center}
.fact{position:absolute;width:291px;filter:drop-shadow(0 2px 4px rgba(0,0,0,.22))}
.fact-body{background:#fff;clip-path:polygon(0 0,100% 0,100% 100%,26px 100%,0 calc(100% - 26px));padding:0 18px;display:flex;align-items:center;justify-content:center;text-align:center;font-size:11.5px;line-height:14.5px;color:#333}
.fact-icon{position:absolute;left:106px;top:-46px;width:80px;height:80px;border-radius:50%;background:#fff;border:4px solid var(--green);display:flex;align-items:center;justify-content:center}
.ongoing{position:absolute;top:1220px;left:0;width:661px;height:264px;background:linear-gradient(90deg,#f2f2f2 0%,#f7f7f7 50%,#e9e9e9 100%)}
.ongoing-tab{position:absolute;left:0;top:0;width:86px;height:264px;background:#3a3a3a;border-radius:0 14px 14px 0;display:flex;align-items:center;justify-content:center}
.ongoing-tab span{transform:rotate(-90deg);color:#fff;font-family:"Montserrat",sans-serif;font-weight:800;font-size:44px;letter-spacing:1px;white-space:nowrap}
.ongoing-text{position:absolute;left:116px;top:20px;width:516px;font-size:11.8px;line-height:14.5px;color:#333;text-align:justify}
.ongoing-list{list-style:none;margin-top:14px}
.ongoing-list li{position:relative;padding-left:38px;margin-bottom:13px}
.ongoing-list svg{position:absolute;left:0;top:0}
.band-green{position:absolute;top:1516px;left:0;width:661px;height:46px;background:var(--green);color:#fff;font-family:"Montserrat",sans-serif;font-weight:700;font-size:24px;display:flex;align-items:center;justify-content:center;gap:12px}
.mapping{position:absolute;top:1567px;left:0;width:661px;height:248px;background:var(--panel)}
.mapping-col{position:absolute;top:18px}
.mapping-col.left{left:52px}
.mapping-col.right{left:370px}
.mapping-divider{position:absolute;left:330px;top:20px;width:1px;height:196px;background:#aaa}
.mapping-head{font-family:"Montserrat",sans-serif;font-weight:700;font-size:22px;color:var(--green);display:flex;align-items:center;gap:12px;height:36px}
.mapping-list{list-style:none;margin-top:14px}
.mapping-list li{display:flex;align-items:center;gap:15px;font-family:"Montserrat",sans-serif;font-size:14.5px;color:#333;height:33px}
.tagline{position:absolute;top:1834px;left:40px;width:581px;text-align:center;font-family:"Montserrat",sans-serif;font-weight:700;font-size:20.5px;line-height:25.5px;color:#8c8c8c}
.shot{position:absolute;width:286px}
.shot-frame{width:286px;border-radius:6px;background:linear-gradient(180deg,#e4e4e4 0%,#f6f6f6 18%,#ffffff 60%,#eaeaea 100%);box-shadow:0 1px 3px rgba(0,0,0,.3)}
.shot-caption{text-align:center;font-size:11px;line-height:14px;color:#333;margin-top:14px}
.footer{position:absolute;bottom:0;left:0;width:661px;height:92px;background:var(--footer);display:flex;align-items:center;justify-content:center;text-align:center;color:var(--green);font-family:"Montserrat",sans-serif;font-weight:700;font-size:19.5px;line-height:25px;letter-spacing:-.3px}
</style>
</head>
<body>
<div class="issue-title">MAY/JUNE NEWSLETTER</div>

<main class="sheet">
  <header class="masthead">
    <div class="brand">
      <div class="brand-name">VERDANT HAUS <span class="brand-dot"></span></div>
      <div class="brand-tag">LEADERS IN ENERGY EFFICIENCY</div>
    </div>
    <div class="contact">
      <div><svg width="17" height="12" viewBox="0 0 17 12"><rect x=".6" y=".6" width="15.8" height="10.8" fill="none" stroke="#3cb54a" stroke-width="1.2"/><path d="M.6 .6 8.5 7 16.4 .6" fill="none" stroke="#3cb54a" stroke-width="1.2"/></svg>INFO@VERDANTHAUS.CO.UK</div>
      <div><svg width="15" height="15" viewBox="0 0 15 15"><circle cx="7.5" cy="7.5" r="6.6" fill="none" stroke="#3cb54a" stroke-width="1.2"/><ellipse cx="7.5" cy="7.5" rx="3" ry="6.6" fill="none" stroke="#3cb54a" stroke-width="1.2"/><path d="M1 7.5h13" stroke="#3cb54a" stroke-width="1.2"/></svg>WWW.VERDANTHAUS.CO.UK</div>
    </div>
  </header>

  <section class="hero" role="img" aria-label="Night photograph of a lit bridge over a river in blue tones">
    <div class="hero-title">ENERGY PERFORMANCE IMPROVEMENT SERVICES</div>
    <div class="hero-sub">LEADERS IN ENERGY EFFICIENCY</div>
  </section>

  <h1 class="section-title">EPC CHALLENGES</h1>

  <section class="april">
    <div class="april-tab">
      <svg width="20" height="20" viewBox="0 0 20 20"><rect x="1.5" y="3" width="17" height="15.5" rx="1.5" fill="none" stroke="#fff" stroke-width="1.6"/><path d="M1.5 7.5h17M6 1v4M14 1v4" stroke="#fff" stroke-width="1.6"/><g fill="#fff"><rect x="4.5" y="10" width="2.4" height="2.2"/><rect x="8.8" y="10" width="2.4" height="2.2"/><rect x="13.1" y="10" width="2.4" height="2.2"/><rect x="4.5" y="14" width="2.4" height="2.2"/><rect x="8.8" y="14" width="2.4" height="2.2"/></g></svg>
      APRIL 2023
    </div>
    <svg class="april-icon" style="left:18px" width="54" height="58" viewBox="0 0 54 58"><path d="M8 4h26v44H4V10" fill="none" stroke="#3cb54a" stroke-width="2"/><path d="M4 10c0-3 2-6 4-6s4 3 4 6H4z" fill="none" stroke="#3cb54a" stroke-width="2"/><path d="M12 16h16M12 23h16M12 30h16M12 37h12" stroke="#3cb54a" stroke-width="2"/><circle cx="40" cy="44" r="10" fill="#fff" stroke="#3cb54a" stroke-width="2"/><path d="M40 38v12M34 44h12" stroke="#3cb54a" stroke-width="2"/></svg>
    <p class="april-col left">From April 2023 existing MEES regulations will be extended to cover all non-domestic tenancies (already in place for domestic tenancies since 1st April 2020).</p>
    <div class="april-divider"></div>
    <svg class="april-icon" style="left:315px" width="48" height="42" viewBox="0 0 48 42"><rect x="1.5" y="1.5" width="45" height="39" rx="4" fill="none" stroke="#3cb54a" stroke-width="2.2"/><circle cx="14" cy="15" r="5" fill="none" stroke="#3cb54a" stroke-width="2"/><path d="M6 30c0-6 4-9 8-9s8 3 8 9z" fill="none" stroke="#3cb54a" stroke-width="2"/><path d="M27 12h14M27 18h14M27 24h14M27 30h14" stroke="#3cb54a" stroke-width="2"/></svg>
    <p class="april-col right">MEES (Minimum Energy Efficiency Standard) regulations make it unlawful to agree a new lease on a property with an EPC rating below an E unless an exemption has been put in place on the PRS register.</p>
  </section>

  <div class="band-grey">BEYOND APRIL 2023</div>

  <article class="fact" style="left:32px;top:758px">
    <div class="fact-body" style="height:170px;padding-top:20px">The UK Governments long term aim of having net zero carbon emissions by 2050 has several key dates before to make this achievable.</div>
    <div class="fact-icon"><svg width="40" height="38" viewBox="0 0 40 38"><path d="M20 2 3 10h34z" fill="none" stroke="#333" stroke-width="2"/><path d="M3 12h34M3 33h34M1 36h38" stroke="#333" stroke-width="2"/><path d="M8 15v15M14 15v15M20 15v15M26 15v15M32 15v15" stroke="#333" stroke-width="2"/></svg></div>
  </article>
  <article class="fact" style="left:335px;top:758px">
    <div class="fact-body" style="height:170px;padding-top:34px">Consultation process closed in January this year into the minimum energy standards for non domestic properties.&nbsp; The consultation process looked into the future trajectory of measures up to 2030, with one suggestion being for commercial properties to be of minimum band C or B.</div>
    <div class="fact-icon"><svg width="44" height="44" viewBox="0 0 44 44"><rect x="18" y="2" width="20" height="12" rx="1" fill="none" stroke="#333" stroke-width="2"/><path d="M26 14v5" stroke="#333" stroke-width="2"/><circle cx="14" cy="16" r="4" fill="none" stroke="#333" stroke-width="2"/><path d="M7 32v-7c0-3 3-5 7-5s6 2 7 4l6 2" fill="none" stroke="#333" stroke-width="2"/><path d="M4 32h36M10 32v9M34 32v9" stroke="#333" stroke-width="2"/></svg></div>
  </article>
  <article class="fact" style="left:32px;top:990px">
    <div class="fact-body" style="height:182px;align-items:flex-start;padding-top:52px">The Clean Growth Strategy is already in place to help as many domestic properties achieve band C by 2035.</div>
    <div class="fact-icon"><svg width="40" height="38" viewBox="0 0 40 38"><path d="M4 36h34" stroke="#333" stroke-width="2"/><rect x="6" y="24" width="6" height="12" fill="none" stroke="#333" stroke-width="2"/><rect x="15" y="18" width="6" height="18" fill="none" stroke="#333" stroke-width="2"/><rect x="24" y="12" width="6" height="24" fill="none" stroke="#333" stroke-width="2"/><path d="M5 18 14 11l6 3 14-11M28 3h6v6" fill="none" stroke="#333" stroke-width="2"/></svg></div>
  </article>
  <article class="fact" style="left:335px;top:990px">
    <div class="fact-body" style="height:182px;padding-top:12px;font-size:11px;line-height:14.5px">The definition is two-pronged. Firstly, during the construction process of an asset, the amount of carbon emissions produced should be zero, or negative through the use of offsets or the export of on-site renewable energy. Secondly, during the use of the building, the amount of carbon emissions produced from the building's operational energy should also be zero or negative.</div>
    <div class="fact-icon"><svg width="44" height="44" viewBox="0 0 44 44"><circle cx="22" cy="22" r="19" fill="none" stroke="#333" stroke-width="2"/><circle cx="22" cy="22" r="6" fill="none" stroke="#333" stroke-width="2"/><path d="M22 9v4M22 31v4M9 22h4M31 22h4M13 13l3 3M28 28l3 3M31 13l-3 3M16 28l-3 3" stroke="#333" stroke-width="2.4"/><circle cx="22" cy="22" r="11" fill="none" stroke="#333" stroke-width="2"/></svg></div>
  </article>

  <section class="ongoing">
    <div role="img" aria-label="Faint photograph of a hand writing on documents" style="position:absolute;inset:0;background:linear-gradient(120deg,transparent 40%,rgba(210,210,210,.35) 70%,transparent 100%)"></div>
    <div class="ongoing-tab"><span>ONGOING</span></div>
    <div class="ongoing-text">
      <p>As part of companies overall commitment to EPC management, companies face the following challenges that need to be proactively managed</p>
      <ul class="ongoing-list">
        <li><svg width="18" height="18" viewBox="0 0 18 18"><circle cx="9" cy="9" r="7.8" fill="none" stroke="#3cb54a" stroke-width="1.6"/><path d="m5 9 3 3 5-6" fill="none" stroke="#3cb54a" stroke-width="1.8"/></svg>EPC expiry dates&nbsp; As EPCs are only valid for 10 years, there is a requirement to ensure that EPC valid dates are managed and in date to ensure that transactions aren't delayed due to have an expired EPC.&nbsp; It also important to ensure these are done in advance as there is sometimes changes in the rating due to more stricter controls being applied.</li>
        <li><svg width="18" height="18" viewBox="0 0 18 18"><circle cx="9" cy="9" r="7.8" fill="none" stroke="#3cb54a" stroke-width="1.6"/><path d="m5 9 3 3 5-6" fill="none" stroke="#3cb54a" stroke-width="1.8"/></svg>Managing low rated properties and improvements.&nbsp;&nbsp; Where properties fail current MEES compliance (F&amp;G), these properties should be identified and managed to ensure that any upcoming PPM or retrofit works are taken into consideration and the impact on the EPC</li>
        <li><svg width="18" height="18" viewBox="0 0 18 18"><circle cx="9" cy="9" r="7.8" fill="none" stroke="#3cb54a" stroke-width="1.6"/><path d="m5 9 3 3 5-6" fill="none" stroke="#3cb54a" stroke-width="1.8"/></svg>Lease end dates</li>
      </ul>
    </div>
  </section>

  <div class="band-green">
    <svg width="46" height="28" viewBox="0 0 46 28"><path d="M1 14h5l3-7 4 13 3-8h4" fill="none" stroke="#fff" stroke-width="2"/><circle cx="30" cy="12" r="9" fill="none" stroke="#fff" stroke-width="2.4"/><path d="m36.5 18.5 7 7" stroke="#fff" stroke-width="3"/></svg>
    EPC MAPPING AND MONITORING
  </div>

  <section class="mapping">
    <div class="mapping-col left">
      <div class="mapping-head"><svg width="30" height="30" viewBox="0 0 30 30" fill="none" stroke="#555" stroke-width="1.4"><circle cx="15" cy="4" r="3"/><path d="M10 13c0-3 2-5 5-5s5 2 5 5zM15 13v4M6 17h18"/><circle cx="6" cy="21" r="2.4"/><circle cx="15" cy="21" r="2.4"/><circle cx="24" cy="21" r="2.4"/><path d="M2 29c0-3 2-4 4-4s4 1 4 4M11 29c0-3 2-4 4-4s4 1 4 4M20 29c0-3 2-4 4-4s4 1 4 4"/></svg>Managing</div>
      <ul class="mapping-list">
        <li><svg width="15" height="15" viewBox="0 0 18 18"><circle cx="9" cy="9" r="7.8" fill="none" stroke="#3cb54a" stroke-width="1.8"/><path d="m5 9 3 3 5-6" fill="none" stroke="#3cb54a" stroke-width="2"/></svg>EPC EXPIRY DATES</li>
        <li><svg width="15" height="15" viewBox="0 0 18 18"><circle cx="9" cy="9" r="7.8" fill="none" stroke="#3cb54a" stroke-width="1.8"/><path d="m5 9 3 3 5-6" fill="none" stroke="#3cb54a" stroke-width="2"/></svg>LEASE END DATES</li>
        <li><svg width="15" height="15" viewBox="0 0 18 18"><circle cx="9" cy="9" r="7.8" fill="none" stroke="#3cb54a" stroke-width="1.8"/><path d="m5 9 3 3 5-6" fill="none" stroke="#3cb54a" stroke-width="2"/></svg>EPC RATINGS</li>
        <li><svg width="15" height="15" viewBox="0 0 18 18"><circle cx="9" cy="9" r="7.8" fill="none" stroke="#3cb54a" stroke-width="1.8"/><path d="m5 9 3 3 5-6" fill="none" stroke="#3cb54a" stroke-width="2"/></svg>EXEMPTIONS</li>
        <li><svg width="15" height="15" viewBox="0 0 18 18"><circle cx="9" cy="9" r="7.8" fill="none" stroke="#3cb54a" stroke-width="1.8"/><path d="m5 9 3 3 5-6" fill="none" stroke="#3cb54a" stroke-width="2"/></svg>EPC RATING PLANNING</li>
      </ul>
    </div>
    <div class="mapping-divider"></div>
    <div class="mapping-col right">
      <div class="mapping-head" style="height:28px">This can be done by:-</div>
      <ul class="mapping-list" style="margin-top:22px">
        <li><svg width="15" height="15" viewBox="0 0 18 18"><circle cx="9" cy="9" r="7.8" fill="none" stroke="#3cb54a" stroke-width="1.8"/><path d="m5 9 3 3 5-6" fill="none" stroke="#3cb54a" stroke-width="2"/></svg>TYPE OF SITE</li>
        <li><svg width="15" height="15" viewBox="0 0 18 18"><circle cx="9" cy="9" r="7.8" fill="none" stroke="#3cb54a" stroke-width="1.8"/><path d="m5 9 3 3 5-6" fill="none" stroke="#3cb54a" stroke-width="2"/></svg>AGE OF SITE</li>
        <li><svg width="15" height="15" viewBox="0 0 18 18"><circle cx="9" cy="9" r="7.8" fill="none" stroke="#3cb54a" stroke-width="1.8"/><path d="m5 9 3 3 5-6" fill="none" stroke="#3cb54a" stroke-width="2"/></svg>LOCATION</li>
        <li><svg width="15" height="15" viewBox="0 0 18 18"><circle cx="9" cy="9" r="7.8" fill="none" stroke="#3cb54a" stroke-width="1.8"/><path d="m5 9 3 3 5-6" fill="none" stroke="#3cb54a" stroke-width="2"/></svg>REGION</li>
        <li><svg width="15" height="15" viewBox="0 0 18 18"><circle cx="9" cy="9" r="7.8" fill="none" stroke="#3cb54a" stroke-width="1.8"/><path d="m5 9 3 3 5-6" fill="none" stroke="#3cb54a" stroke-width="2"/></svg>PORTFOLIO</li>
      </ul>
    </div>
  </section>

  <p class="tagline">Verdant Haus have developed a market leading EPC management tool to meet the current and ongoing EPC challenges faced in the property market.</p>

  <figure class="shot" style="left:33px;top:1949px">
    <div class="shot-frame" style="height:186px" role="img" aria-label="Screenshot of the VHConnect dashboard with rating tiles and a bar chart"></div>
    <figcaption class="shot-caption">VHConnect Dashboard - View</figcaption>
  </figure>
  <figure class="shot" style="left:341px;top:1949px">
    <div class="shot-frame" style="height:186px" role="img" aria-label="Screenshot of the VHConnect search results table"></div>
    <figcaption class="shot-caption">VHConnect – Search functionality view</figcaption>
  </figure>
  <figure class="shot" style="left:33px;top:2181px">
    <div class="shot-frame" style="height:176px;background:linear-gradient(180deg,#e4e4e4 0%,#9a9a9a 15%,#ffffff 16%,#f4f4f4 90%,#9a9a9a 100%)" role="img" aria-label="Screenshot of the VHConnect EPC details pop-up window"></div>
    <figcaption class="shot-caption">VHConnect – View EPC screen</figcaption>
  </figure>
  <figure class="shot" style="left:341px;top:2181px">
    <div class="shot-frame" style="height:174px" role="img" aria-label="Screenshot of the VHConnect portfolio management page"></div>
    <figcaption class="shot-caption">VHConnect – Portfolio Management view</figcaption>
  </figure>
  <figure class="shot" style="left:188px;top:2408px">
    <div class="shot-frame" style="height:182px" role="img" aria-label="Screenshot of the VHConnect advanced search table"></div>
    <figcaption class="shot-caption">VHConnect – Advanced search functionality –<br>more enhanced than National Database</figcaption>
  </figure>

  <footer class="footer">We are currently offering free trials on VHConnect to demonstrate<br>how we can assist to manage the above challenges.</footer>
</main>
</body>
</html>
```